Chauffeur Car Driver Needing a design with/without logo for business cards

I'm a chauffeur car driver in Melbourne Australia. I have an extensive list of personal customers and need to provide a professional business card to new customers.
My business name is 'RivaPlus'.
I offer a personalised service to customer who need a transport alternative to taxis. I don't want it to look too 'upmarket' as i don't want it to seem too expensive or only for special occasions. The majority of my clients are business professionals who use me for airport transfers.
I definitely don't want the card/logo to have an image of a car/road etc. I prefer something abstract. A 'pencil-line'-type font will grab my attention but not absolutely necessary. Not too 'digital' or 'ultra - modern' looking.
I need the card to display the following information
Riva Plus - main logo/text
Chauffeur Cars - sub text
Marco Devilles
0452 918 306
bookings@RivaPlus.example.au
I would like the focus to be on 'RivaPlus' with everything else smaller.
Look forward to seeing ideas!!!!
Target Market(s)
Business Corporate Professionals
Industry/Entity Type
Airport
Requirements
Nice to have
- Pencil line type font
Should not have
- Images of cars, road, tyres, steering wheel etc.

```html
<!DOCTYPE html>
<html lang="en">
<head>
<meta charset="utf-8">
<title>RivaPlus – Chauffeur Cars Business Card</title>
<link href="https://fonts.googleapis.com/css2?family=Federo&display=swap" rel="stylesheet">
<style>
  :root {
    --frame: #383838;
    --red-edge: #ee3035;
    --red-mid: #9a3034;
    --core: #333333;
    --ink: #ffffff;
  }
  html, body {
    margin: 0;
    padding: 0;
    width: 1200px;
    height: 636px;
    overflow: hidden;
    background: var(--frame);
  }
  .card {
    position: absolute;
    left: 8px;
    top: 8px;
    width: 1184px;
    height: 620px;
    overflow: hidden;
    background: radial-gradient(circle at 596px 313px,
      var(--core) 0px,
      var(--core) 50px,
      #4a3335 160px,
      #6a3235 290px,
      var(--red-mid) 420px,
      #c8323a 560px,
      var(--red-edge) 700px);
    font-family: "Federo", sans-serif;
    color: var(--ink);
  }
  .details {
    position: absolute;
    left: 17px;
    top: 14px;
    margin: 0;
    font-size: 35px;
    line-height: 50px;
    letter-spacing: 0.5px;
    word-spacing: 6px;
  }
  .details p { margin: 0; }
  .details .email { font-size: 33px; line-height: 44px; }
  .brand-name {
    position: absolute;
    left: 0;
    width: 1184px;
    top: 488px;
    margin: 0;
    text-align: center;
    font-size: 84px;
    line-height: 90px;
    font-weight: normal;
    letter-spacing: 1px;
  }
  .brand-rule {
    position: absolute;
    left: 126px;
    top: 587px;
    width: 952px;
    height: 3px;
    background: var(--ink);
  }
</style>
</head>
<body>
  <main class="card">
    <div class="details">
      <p class="service">Chauffeur Cars</p>
      <p class="name">Marco Devilles</p>
      <p class="phone">0452 918 306</p>
      <p class="email">bookings@RivaPlus.example.au</p>
    </div>
    <h1 class="brand-name">RivaPlus</h1>
    <div class="brand-rule"></div>
  </main>
</body>
</html>
```